Pizza Box 10" x 10" - color: White

Custom design, utilizing CrustVarto Logo and include the following information on the Pizza Box:

1. Custom Crafted Pizza with Quality Ingredients.
2. [....Get Your GAME ON] to be placed on the front flap and seen when the
box is opened.
3. You"ll miss 100% of the Pizza you don't eat.

4. Visit www.plenovacartons.example for additional design resource information. Go to site and then click on ORDERING to access.

5. The 10" x 10" Pizza Box is to be in the color WHITE.
6. Use colors Black and Red. no generic images. no food pics. I am looking for a clean and cool design.

Target Market(s)

Age 16 - 36 years

Industry/Entity Type

American Restaurant

Font styles to use
Sans Serif

Colors
ec1f27
000000
ffffff

Requirements
Must have
• Color Red and Black.
• Logo on Top and all sides of the Pizza Box.
Nice to have
• A Creative design that does not look generic.
Should not have
• No food images.

```html
<!DOCTYPE html>
<html lang="en">
<head>
<meta charset="utf-8">
<title>CrustVarto 10" Pizza Box Dieline</title>
<link rel="stylesheet" href="https://fonts.googleapis.com/css2?family=Ubuntu:wght@700&display=swap">
<style>
  :root {
    --backdrop: #888888;
    --board: #ffffff;
    --brand-red: #ec1f27;
    --ink: #000000;
    --die-line: #3a3a3a;
  }
  html, body {
    margin: 0;
    padding: 0;
    width: 1200px;
    height: 1200px;
    overflow: hidden;
    background: var(--backdrop);
  }
  .dieline { display: block; width: 1200px; height: 1200px; }
  .board { fill: var(--board); stroke: var(--die-line); stroke-width: 1.2; stroke-linejoin: round; }
  .cut { fill: none; stroke: var(--die-line); stroke-width: 1.2; }
  .fold { fill: none; stroke: var(--die-line); stroke-width: 1; stroke-dasharray: 5 4; }
  .brand-name { font-family: "Ubuntu", sans-serif; font-weight: 700; fill: var(--ink); }
  .brand-dot { fill: var(--brand-red); }
  .slogan { font-family: "Ubuntu", sans-serif; font-weight: 700; fill: var(--brand-red); font-size: 26px; }
  .game-line { font-family: "Ubuntu", sans-serif; font-weight: 700; fill: var(--brand-red); font-size: 17px; text-anchor: middle; dominant-baseline: central; }
  .tagline { font-family: "Ubuntu", sans-serif; font-weight: 700; fill: var(--ink); font-size: 14px; text-anchor: middle; }
</style>
</head>
<body>
<svg class="dieline" viewBox="0 0 1200 1200" xmlns="http://www.w3.org/2000/svg">
  <!-- box outline -->
  <path class="board" d="
    M298,65 L375,65 L385,57 L490,57 L495,63 L645,63 L650,57 L755,57 L765,65 L836,65
    L836,820 L818,832 L818,948 L836,958 L836,1040 L790,1085 L757,1085 L757,1115
    L720,1162 L415,1162 L375,1115 L375,1085 L345,1085 L298,1045 L298,965 L318,955
    L318,860 L298,825 Z"/>

  <!-- top lid tuck flap -->
  <path class="cut" d="M375,65 L375,132 A6,6 0 0 0 387,132 L387,145"/>
  <path class="cut" d="M765,65 L765,132 A6,6 0 0 1 753,132 L753,145"/>
  <line class="fold" x1="370" y1="135" x2="765" y2="135"/>
  <line class="fold" x1="370" y1="147" x2="765" y2="147"/>
  <circle class="board" cx="566" cy="140" r="18"/>
  <path class="cut" d="M370,147 L370,225 L430,225 L435,232 L490,232 L495,225 L640,225 L645,232 L710,232 L715,225 L765,225 L765,147"/>

  <!-- lid panel and side flaps -->
  <line class="cut" x1="298" y1="228" x2="370" y2="228"/>
  <line class="cut" x1="765" y1="228" x2="836" y2="228"/>
  <line class="fold" x1="370" y1="232" x2="370" y2="620"/>
  <line class="fold" x1="762" y1="232" x2="762" y2="620"/>
  <line class="cut" x1="298" y1="620" x2="370" y2="620"/>
  <line class="cut" x1="762" y1="620" x2="836" y2="620"/>

  <!-- back wall band -->
  <path class="cut" d="M370,620 L370,690 L378,700 L430,700 L435,692 L490,692 L495,700 L620,700 L625,690 L700,690 L705,700 L757,700 L762,690 L762,620"/>
  <line class="fold" x1="370" y1="622" x2="762" y2="622"/>
  <line class="cut" x1="298" y1="720" x2="375" y2="700"/>
  <line class="cut" x1="836" y1="720" x2="757" y2="700"/>

  <!-- base panel -->
  <line class="fold" x1="375" y1="700" x2="375" y2="1085"/>
  <line class="fold" x1="757" y1="700" x2="757" y2="1085"/>
  <path class="fold" d="M375,1085 L545,1085 A20,10 0 0 0 585,1085 L757,1085"/>
  <path class="cut" d="M368,912 L368,1005 M765,912 L765,1005"/>

  <!-- lid tuck name -->
  <g class="brand-lockup">
    <circle class="brand-dot" cx="466" cy="187" r="12"/>
    <text class="brand-name" x="486" y="200" font-size="36">CrustVarto</text>
  </g>

  <!-- side flap names -->
  <g transform="translate(333,520) rotate(-90)">
    <circle class="brand-dot" cx="0" cy="0" r="11"/>
    <text class="brand-name" x="20" y="13" font-size="34">CrustVarto</text>
  </g>
  <g transform="translate(799,325) rotate(90)">
    <circle class="brand-dot" cx="0" cy="0" r="11"/>
    <text class="brand-name" x="20" y="13" font-size="34">CrustVarto</text>
  </g>

  <!-- back wall name (upside down) -->
  <g transform="translate(663,656) rotate(180)">
    <circle class="brand-dot" cx="0" cy="0" r="12"/>
    <text class="brand-name" x="20" y="13" font-size="36">CrustVarto</text>
  </g>

  <!-- main base name -->
  <g class="brand-lockup">
    <circle class="brand-dot" cx="434" cy="792" r="24"/>
    <text class="brand-name" x="470" y="810" font-size="52">CrustVarto</text>
  </g>

  <!-- tagline -->
  <text class="tagline" x="650" y="850">Custom Crafted Pizza</text>
  <text class="tagline" x="650" y="868">with Quality Ingredients</text>

  <!-- slogan -->
  <g class="slogan-block">
    <text class="slogan" x="402" y="922">You"ll miss</text>
    <text class="slogan" x="402" y="960">100% of</text>
    <text class="slogan" x="402" y="998">the pizza</text>
    <text class="slogan" x="402" y="1036">you don't eat.</text>
  </g>

  <!-- Get Your GAME ON lines -->
  <text class="game-line" transform="translate(342,883) rotate(90)">....Get Your GAME ON</text>
  <text class="game-line" transform="translate(794,883) rotate(-90)">....Get Your GAME ON</text>
  <text class="game-line" x="564" y="1123">....Get Your GAME ON</text>
</svg>
</body>
</html>
```